Flyer for the Radiant Harvest Worship Day 2020

I am looking to create a flyer for a one day prayer retreat our church is organizing.
This flyer will be posted on social media, websites and will also be printed so it can be mailed to people.
I am looking for something professional, with good use of our logo and band colors (logo colors).
I am counting on the designer's skill, creativity, art and knowledge of media communication to produce a flyer that will effectively and quickly convey the message we are trying to spread.
CONTENT OF THE FLYER:
Event title: Radiant Harvest Worship Day
Date: Tuesday July 2nd, 2020
Time: 11:00AM - 7:00PM
Maplewood Hotel, 4817 Birchfield Avenue, Portland, Maine 04109 (Room: Evergreen)
Event Key words to highlight what the event is about: Prayer, Sharing the Word, Panel discussion, prophecy, Impartation.
Key phrases:
A one day prayer retreat.
Jesus Chris is Lord
Contact info:
www.tolvex.org
Phone: 207 555 0143
Email: contact@brookmeadow.org

```html
<!DOCTYPE html>
<html lang="en">
<head>
<meta charset="utf-8">
<title>Radiant Harvest Worship Day 2020</title>
<link rel="stylesheet" href="https://fonts.googleapis.com/css2?family=Sorts+Mill+Goudy&display=swap">
<style>
  :root {
    --ink: #000000;
    --paper: #ffffff;
    --amber: #f7941d;
    --amber-light: #fbb34c;
    --amber-deep: #ee7d11;
    --sky-top: #3b2a33;
    --sky-mid: #b4583a;
    --sky-glow: #ee8a3a;
    --sky-low: #c8582a;
    --frame: rgba(255,255,255,0.85);
  }
  html, body {
    margin: 0;
    padding: 0;
    width: 707px;
    height: 1200px;
    overflow: hidden;
    background: var(--ink);
  }
  .flyer {
    position: relative;
    width: 707px;
    height: 1200px;
    background: var(--ink);
    font-family: "Sorts Mill Goudy", Georgia, serif;
    color: var(--paper);
    overflow: hidden;
  }
  .hero-photo {
    position: absolute;
    left: 0; top: 0;
    width: 707px;
    height: 690px;
    background:
      radial-gradient(ellipse 60% 30% at 75% 62%, rgba(255,170,70,0.55), rgba(255,170,70,0) 70%),
      linear-gradient(180deg, var(--sky-top) 0%, #5a3438 18%, var(--sky-mid) 40%, var(--sky-glow) 62%, var(--sky-low) 78%, #2a120a 90%, var(--ink) 100%);
  }
  .frame {
    position: absolute;
    left: 20px; top: 24px; right: 20px; bottom: 24px;
    border: 1px solid var(--frame);
    pointer-events: none;
  }
  .brand {
    position: absolute;
    left: 70px; top: 128px;
    font-size: 62px;
    letter-spacing: 1px;
    color: var(--paper);
    line-height: 1;
  }
  .event-title {
    position: absolute;
    left: 70px; top: 325px;
    margin: 0;
    font-weight: 400;
    font-size: 64px;
    line-height: 84px;
    letter-spacing: 0.5px;
    color: var(--paper);
  }
  .event-date {
    position: absolute;
    left: 0; right: 0; top: 720px;
    display: flex;
    justify-content: center;
    align-items: center;
    gap: 18px;
    font-size: 40px;
    line-height: 1;
  }
  .event-time {
    position: absolute;
    left: 104px; top: 786px;
    width: 500px; height: 68px;
    border-radius: 34px;
    background: linear-gradient(180deg, var(--amber-light) 0%, var(--amber) 55%, var(--amber-deep) 100%);
    display: flex;
    justify-content: center;
    align-items: center;
    gap: 22px;
    font-size: 42px;
    color: var(--paper);
    line-height: 1;
  }
  .venue-name {
    position: absolute;
    left: 0; right: 0; top: 880px;
    text-align: center;
    font-size: 25px;
    color: var(--amber);
  }
  .venue-address {
    position: absolute;
    left: 0; right: 0; top: 920px;
    text-align: center;
    font-size: 18px;
  }
  .rule {
    position: absolute;
    left: 68px; right: 68px;
    height: 1px;
    background: var(--amber);
  }
  .rule-top { top: 964px; }
  .rule-bottom { top: 1102px; }
  .keywords-label {
    position: absolute;
    left: 0; right: 0; top: 982px;
    text-align: center;
    font-size: 16px;
    color: var(--amber);
  }
  .keywords {
    position: absolute;
    left: 0; right: 0; top: 1010px;
    text-align: center;
    font-size: 17px;
  }
  .phrases {
    position: absolute;
    left: 0; right: 0; top: 1050px;
    display: flex;
    justify-content: center;
    align-items: center;
    gap: 8px;
    font-size: 14px;
  }
  .phrases-label {
    font-size: 19px;
    color: var(--amber);
    margin-right: 2px;
  }
  .contacts {
    position: absolute;
    left: 68px; right: 68px; top: 1126px;
    display: flex;
    justify-content: space-between;
    align-items: center;
    font-size: 17px;
  }
  .contact-item {
    display: flex;
    align-items: center;
    gap: 6px;
  }
  .icon { display: block; }
</style>
</head>
<body>
<main class="flyer">
  <div class="hero-photo" role="img" aria-label="Sunset sky over a dark hill with a wooden cross draped in purple cloth"></div>

  <div class="brand">TOLVEX</div>

  <h1 class="event-title">RADIANT<br>HARVEST<br>WORSHIP DAY</h1>

  <div class="event-date">
    <svg class="icon" width="38" height="38" viewBox="0 0 38 38" fill="none" stroke="#f7941d" stroke-width="1.8">
      <rect x="3" y="7" width="30" height="26" rx="3"/>
      <line x1="3" y1="14" x2="33" y2="14"/>
      <line x1="10" y1="3" x2="10" y2="10"/>
      <line x1="18" y1="3" x2="18" y2="10"/>
      <line x1="26" y1="3" x2="26" y2="10"/>
      <rect x="8" y="18" width="4" height="3"/><rect x="15" y="18" width="4" height="3"/><rect x="22" y="18" width="4" height="3"/>
      <rect x="8" y="25" width="4" height="3"/><rect x="15" y="25" width="4" height="3"/>
      <circle cx="29" cy="29" r="6" fill="#000"/>
      <polyline points="26,29 28.5,31.5 32,27"/>
    </svg>
    <span>Tuesday July 2nd, 2020</span>
  </div>

  <div class="event-time">
    <svg class="icon" width="38" height="38" viewBox="0 0 38 38" fill="none" stroke="#ffffff" stroke-width="2">
      <circle cx="19" cy="19" r="16"/>
      <polyline points="19,9 19,19 26,22"/>
    </svg>
    <span>11:00AM - 7:00PM</span>
  </div>

  <div class="venue-name">Maplewood Hotel</div>
  <div class="venue-address">4817 Birchfield Avenue, Portland, Maine 04109 (Room: Evergreen)</div>

  <div class="rule rule-top"></div>

  <div class="keywords-label">Event Key words to highlight what the event is about:</div>
  <div class="keywords">Prayer, Sharing the Word, Panel discussion, prophecy, Impartation.</div>

  <div class="phrases">
    <span class="phrases-label">Key Phrases:</span>
    <svg class="icon" width="12" height="12" viewBox="0 0 12 12" fill="none" stroke="#f7941d" stroke-width="1.2"><circle cx="6" cy="6" r="5"/><polyline points="3.5,6 5.3,7.8 8.5,4.3"/></svg>
    <span>A one day prayer retreat.</span>
    <svg class="icon" width="12" height="12" viewBox="0 0 12 12" fill="none" stroke="#f7941d" stroke-width="1.2"><circle cx="6" cy="6" r="5"/><polyline points="3.5,6 5.3,7.8 8.5,4.3"/></svg>
    <span>Jesus Chris is Lord</span>
  </div>

  <div class="rule rule-bottom"></div>

  <div class="contacts">
    <div class="contact-item">
      <svg class="icon" width="12" height="12" viewBox="0 0 12 12" fill="none" stroke="#f7941d" stroke-width="1"><circle cx="6" cy="6" r="5"/><ellipse cx="6" cy="6" rx="2.2" ry="5"/><line x1="1" y1="6" x2="11" y2="6"/></svg>
      <span>www.tolvex.org</span>
    </div>
    <div class="contact-item">
      <svg class="icon" width="13" height="13" viewBox="0 0 13 13" fill="none" stroke="#f7941d" stroke-width="1.1"><circle cx="6.5" cy="6.5" r="5.5"/><path d="M4.5 3.5 L5.5 5 L4.8 5.8 Q5.5 7.5 7.2 8.2 L8 7.5 L9.5 8.5 L8.8 9.6 Q5 9.5 3.5 4.3 Z"/></svg>
      <span>207 555 0143</span>
    </div>
    <div class="contact-item">
      <svg class="icon" width="13" height="10" viewBox="0 0 13 10" fill="none" stroke="#f7941d" stroke-width="1"><rect x="0.5" y="0.5" width="12" height="9"/><polyline points="0.5,0.5 6.5,5.5 12.5,0.5"/></svg>
      <span>contact@brookmeadow.org</span>
    </div>
  </div>

  <div class="frame"></div>
</main>
</body>
</html>
```